Harold Brisk Mechanical business cards

We need business cards designed for "Harold Brisk Mechanical" "Mechanical & Electrical Contractors" "Specializing in Service & Installation"
"Cooling, Heating, Service, Installations, Residential, Commercial"

```html
<!DOCTYPE html>
<html lang="en">
<head>
<meta charset="utf-8">
<title>Harold Brisk Mechanical – Business Cards</title>
<link href="https://fonts.googleapis.com/css2?family=Lato:wght@400;700;900&display=swap" rel="stylesheet">
<style>
  :root{
    --bg:#e6e6e6;
    --black:#111111;
    --charcoal:#2b2b2b;
    --red:#d9202c;
    --paper:#f4f4f2;
    --white:#ffffff;
    --ink:#1c1c1c;
  }
  *{box-sizing:border-box;margin:0;padding:0}
  html,body{width:1200px;height:900px;overflow:hidden;background:var(--bg)}
  body{position:relative;font-family:'Lato',Arial,sans-serif}
  .card{position:absolute;width:640px;height:366px;overflow:hidden;box-shadow:0 6px 18px rgba(0,0,0,.25)}
  .card--back{left:80px;top:60px;background:var(--black);color:var(--white)}
  .card--front{left:480px;top:474px;background:var(--paper);color:var(--ink)}

  .brand{position:absolute;display:flex;align-items:center;gap:12px;font-weight:900;font-size:22px;letter-spacing:.5px;text-transform:uppercase;line-height:1.1}
  .brand__mark{width:40px;height:40px;background:var(--red);flex:none}
  .card--back .brand{right:42px;top:150px;color:var(--white);width:250px}
  .card--front .brand{right:34px;top:42px;color:var(--ink);width:240px}

  .services{position:absolute;left:48px;top:96px}
  .services__heading{color:var(--red);font-size:16px;font-weight:700;margin-bottom:14px}
  .services__list{list-style:none}
  .services__item{display:flex;align-items:center;gap:8px;font-size:17px;margin-bottom:8px}
  .services__item svg{width:18px;height:18px;flex:none}

  .card__shapes{position:absolute;inset:0;width:640px;height:366px}
  .person{position:absolute;left:40px;top:112px}
  .person__name{font-size:24px;font-weight:900;letter-spacing:.3px}
  .person__title{color:var(--red);font-size:15px;margin-top:4px;padding-bottom:6px;border-bottom:2px solid var(--red);display:inline-block;width:110px}

  .contact{position:absolute;left:40px;color:var(--white);font-size:16px;list-style:none}
  .contact--phones{top:200px}
  .contact--web{top:268px}
  .contact li{display:flex;align-items:center;gap:10px;height:22px;margin-bottom:6px}
  .contact__icon{width:22px;height:22px;border-radius:4px;background:var(--red);display:flex;align-items:center;justify-content:center;flex:none}
  .contact__icon svg{width:14px;height:14px}

  .social{position:absolute;right:40px;top:252px;display:flex;gap:14px}
  .social span{width:22px;height:22px;border-radius:4px;background:var(--ink);display:block}
</style>
</head>
<body>

<section class="card card--back" aria-label="Card back">
  <div class="services">
    <p class="services__heading">Specializing in Service &amp; Installation</p>
    <ul class="services__list">
      <li class="services__item"><svg viewBox="0 0 18 18"><rect x="1" y="4" width="12" height="12" fill="none" stroke="#d9202c" stroke-width="2"/><path d="M4 9l4 4 9-11" fill="none" stroke="#d9202c" stroke-width="2.4"/></svg>Cooling</li>
      <li class="services__item"><svg viewBox="0 0 18 18"><rect x="1" y="4" width="12" height="12" fill="none" stroke="#d9202c" stroke-width="2"/><path d="M4 9l4 4 9-11" fill="none" stroke="#d9202c" stroke-width="2.4"/></svg>Heating</li>
      <li class="services__item"><svg viewBox="0 0 18 18"><rect x="1" y="4" width="12" height="12" fill="none" stroke="#d9202c" stroke-width="2"/><path d="M4 9l4 4 9-11" fill="none" stroke="#d9202c" stroke-width="2.4"/></svg>Service</li>
      <li class="services__item"><svg viewBox="0 0 18 18"><rect x="1" y="4" width="12" height="12" fill="none" stroke="#d9202c" stroke-width="2"/><path d="M4 9l4 4 9-11" fill="none" stroke="#d9202c" stroke-width="2.4"/></svg>Installations</li>
      <li class="services__item"><svg viewBox="0 0 18 18"><rect x="1" y="4" width="12" height="12" fill="none" stroke="#d9202c" stroke-width="2"/><path d="M4 9l4 4 9-11" fill="none" stroke="#d9202c" stroke-width="2.4"/></svg>Residential</li>
      <li class="services__item"><svg viewBox="0 0 18 18"><rect x="1" y="4" width="12" height="12" fill="none" stroke="#d9202c" stroke-width="2"/><path d="M4 9l4 4 9-11" fill="none" stroke="#d9202c" stroke-width="2.4"/></svg>Commercial</li>
    </ul>
  </div>
  <div class="brand"><span class="brand__mark"></span>Harold Brisk Mechanical</div>
</section>

<section class="card card--front" aria-label="Card front">
  <svg class="card__shapes" viewBox="0 0 640 366" aria-hidden="true">
    <path d="M0 188 H300 L350 212 H440 V332 H0 Z" fill="#2b2b2b"/>
    <path d="M0 332 H420 Q440 332 440 312 V236 Q440 222 454 220 L472 204 H640 V346 H0 Z" fill="#d9202c"/>
    <line x1="0" y1="260" x2="440" y2="260" stroke="#ffffff" stroke-width="2"/>
  </svg>

  <div class="brand"><span class="brand__mark"></span>Harold Brisk Mechanical</div>

  <div class="person">
    <p class="person__name">HAROLD BRISK</p>
    <p class="person__title">JOB TITLE</p>
  </div>

  <ul class="contact contact--phones">
    <li><span class="contact__icon"><svg viewBox="0 0 14 14"><path d="M3 1l2 3-1.5 1.5a7 7 0 0 0 5 5L10 9l3 2-1 2.5C6 13 1 8 .8 2z" fill="#fff"/></svg></span>000 000 0000</li>
    <li><span class="contact__icon"><svg viewBox="0 0 14 14"><rect x="3.5" y="1" width="7" height="12" rx="1.5" fill="none" stroke="#fff" stroke-width="1.6"/><circle cx="7" cy="10.8" r=".9" fill="#fff"/></svg></span>000 000 0000</li>
  </ul>
  <ul class="contact contact--web">
    <li><span class="contact__icon"><svg viewBox="0 0 14 14"><rect x="1" y="3" width="12" height="8" fill="none" stroke="#fff" stroke-width="1.5"/><path d="M1 3l6 5 6-5" fill="none" stroke="#fff" stroke-width="1.5"/></svg></span>youremail@yxz.com</li>
    <li><span class="contact__icon"><svg viewBox="0 0 14 14"><circle cx="7" cy="7" r="5.5" fill="none" stroke="#fff" stroke-width="1.4"/><path d="M1.5 7h11M7 1.5c-3 3.5-3 7.5 0 11M7 1.5c3 3.5 3 7.5 0 11" fill="none" stroke="#fff" stroke-width="1.2"/></svg></span>www.yourwebsite.com</li>
  </ul>

  <div class="social" aria-label="Social profiles"><span></span><span></span><span></span><span></span></div>
</section>

</body>
</html>
```